Regionale Imkerei sucht Etiketten-Design
Sehr gutes Endergebnis. Hochprofessionelle Abwicklung. Hat jeden Änderungswunsch zügig umgesetzt. Sehr angenehme, zielorientierte Kommunikation. Wirklich zu empfehlen, gerne wieder!
Zielgruppe
Mein Vater und ich haben eine regionale Hobbyimkerei, die wir nach und nach ausbauen wollen. Seit 1949 imkert unsere Familie. Ich bin in dritter Generation eingestiegen und möchte neben meinem know-how den Verkauf und das Marketing voran treiben um mit der Imkerei einen Nebenerwerb zu schaffen. Unsere Zielgruppe sind bewusste Verbraucher/innen, die gerne regional, hochqualitativ und nachhaltig einkaufen. Die meisten Honiggläser verkaufen wir direkt an der Haustür. Bis jetzt sind nur zwei Läden beliefert. Das soll sich dank musterwerkstatt ändern.
Aufgabenstellung
Ich habe eine Ausschreibung im PDF Format verfasst und beigefügt.
Was dort fehlt sind die Lagerungshinweise: kühl, trocken und dunkel lagern.
Für weitere Rückfragen gerne melden.

```html
<!DOCTYPE html>
<html lang="de">
<head>
<meta charset="utf-8">
<title>Tannenfrost Honig – Etiketten</title>
<link rel="stylesheet" href="https://fonts.googleapis.com/css2?family=Montserrat:wght@400;500;600;700&family=Kaushan+Script&display=swap">
<style>
  :root {
    --gold: #bf9a52;
    --gold-soft: #d8bf8c;
    --comb: #faf5ea;
    --pink: #d4007a;
    --orange: #f28c00;
    --green: #8dc63f;
    --grey: #8a8a8a;
    --paper: #ffffff;
  }
  * { box-sizing: border-box; margin: 0; padding: 0; }
  html, body { width: 779px; height: 1200px; overflow: hidden; background: var(--paper); }
  body { position: relative; font-family: "Montserrat", sans-serif; color: var(--gold); }

  .swatches { position: absolute; top: 26px; left: 674px; display: flex; gap: 10px; }
  .swatch { width: 16px; height: 16px; }
  .swatch--orange { background: var(--orange); }
  .swatch--pink { background: var(--pink); }
  .swatch--green { background: var(--green); }

  .seal { position: absolute; left: 311px; top: 65px; width: 144px; height: 144px; border-radius: 50%;
    background: var(--paper); box-shadow: 0 3px 14px rgba(0,0,0,.12); }
  .seal svg { position: absolute; inset: 0; }
  .seal__claim { position: absolute; top: 74px; width: 100%; text-align: center; font-size: 11px; font-weight: 500; line-height: 13px; letter-spacing: .3px; }
  .seal__dot { position: absolute; left: 64px; top: 40px; width: 16px; height: 16px; border-radius: 50%; background: var(--gold); }
  .seal-band { position: absolute; left: 365px; top: 208px; width: 38px; height: 84px; background: var(--pink); }
  .seal-band span { position: absolute; left: 50%; top: 50%; transform: translate(-50%,-50%) rotate(-90deg);
    white-space: nowrap; color: #fff; font-size: 5.5px; font-weight: 700; letter-spacing: .4px; }

  .seal-note { position: absolute; left: 500px; top: 180px; width: 120px; text-align: center;
    font-size: 8.5px; letter-spacing: 1.6px; color: var(--grey); line-height: 12.5px; }
  .seal-arrow { position: absolute; left: 470px; top: 132px; }

  .label { position: absolute; left: 96px; width: 575px; height: 141px; background: var(--paper);
    box-shadow: 0 0 0 1px #eeeeee, 0 2px 6px rgba(0,0,0,.05); --accent: var(--pink); }
  .label--orange { --accent: var(--orange); }
  .label--green { --accent: var(--green); }
  .label__comb { position: absolute; left: 180px; top: 12px; width: 215px; height: 118px;
    background: radial-gradient(ellipse at center, var(--comb) 0%, rgba(250,245,234,.4) 60%, rgba(255,255,255,0) 100%); }
  .col { position: absolute; top: 0; text-align: center; font-size: 7.3px; line-height: 9.1px; }
  .col--info { left: 15px; width: 158px; }
  .col--facts { left: 402px; width: 154px; }
  .col--brand { left: 187px; width: 200px; }
  .col__head { position: absolute; top: 12px; width: 100%; font-weight: 700; color: var(--accent); font-size: 7.5px; }
  .col__text { position: absolute; top: 31px; width: 100%; }
  .col__text b { font-weight: 700; }
  .col__rule { position: absolute; top: 93px; left: 36px; width: 86px; height: 1px; background: linear-gradient(90deg, transparent, var(--gold), transparent); }
  .col__address { position: absolute; top: 103px; width: 100%; }
  .col__web { font-weight: 700; color: var(--accent); }

  .brand__mark { position: absolute; top: 9px; left: 92px; width: 16px; height: 16px; border-radius: 50%; background: var(--gold); }
  .brand__name { position: absolute; top: 37px; width: 100%; font-size: 16px; font-weight: 500; letter-spacing: .6px; line-height: 18px; }
  .brand__rule { position: absolute; top: 57px; left: 48px; width: 104px; height: 1px; background: var(--gold-soft); }
  .brand__tag { position: absolute; top: 61px; width: 100%; font-size: 5.6px; letter-spacing: 1px; font-weight: 500; }
  .brand__variety { position: absolute; top: 70px; width: 100%; font-family: "Kaushan Script", cursive; font-size: 28px; line-height: 34px; }
  .brand__note { position: absolute; top: 104px; width: 100%; font-size: 7px; }
  .brand__web { position: absolute; top: 120px; width: 100%; font-size: 7.3px; font-weight: 700; letter-spacing: .6px; }

  .facts__line { position: absolute; width: 100%; }
  .facts__weight { font-size: 14px; font-weight: 700; line-height: 16px; }
  .facts__box { position: absolute; top: 105px; left: 29px; width: 96px; height: 22px; border: 1px solid var(--gold); }

  .footer { position: absolute; top: 1122px; width: 100%; text-align: center; font-size: 6.5px; letter-spacing: 1.3px; color: var(--grey); }
</style>
</head>
<body>

<div class="swatches">
  <div class="swatch swatch--orange"></div>
  <div class="swatch swatch--pink"></div>
  <div class="swatch swatch--green"></div>
</div>

<div class="seal-band"><span>100% NATUR-HONIG</span></div>
<div class="seal">
  <svg width="144" height="144" viewBox="0 0 144 144">
    <defs><path id="sealRing" d="M72,72 m-57,0 a57,57 0 1,1 114,0 a57,57 0 1,1 -114,0"/></defs>
    <text font-family="Montserrat, sans-serif" font-size="5.6" fill="#bf9a52" letter-spacing="1.1">
      <textPath href="#sealRing">WWW.TANNENFROST.DE · TANNENFROST · E. HALLBERGER · LINDENAUER STR. 14 · 74100 WIESENTAL ·</textPath>
    </text>
  </svg>
  <div class="seal__dot"></div>
  <div class="seal__claim">FÜR GOLDENE<br>MOMENTE</div>
</div>

<svg class="seal-arrow" width="78" height="36" viewBox="0 0 78 36">
  <path d="M72 32 C55 14, 35 8, 6 9" fill="none" stroke="#777" stroke-width="1"/>
  <path d="M11 5 L5 9 L11 13" fill="none" stroke="#777" stroke-width="1"/>
</svg>
<div class="seal-note">QUALITÄTSSIEGEL<br>56 MM DURCHMESSER</div>

<!-- Label template repeated per variety -->
<section class="label" style="top:292px">
  <div class="label__comb" role="img" aria-label="Dezentes Wabenmuster im Hintergrund"></div>
  <div class="col col--info">
    <div class="col__head">Bienenhonig aus der Region</div>
    <p class="col__text">Honig ist ein reines Naturprodukt ohne Zusätze. Diese Reinheit und Natürlichkeit sind in <b>Tannenfrost-Honig</b> vereint. Geniessen Sie goldene Momente mit ökologischem Natur-Honig aus eigener Ernte und regionalem Ursprung.</p>
    <div class="col__rule"></div>
    <p class="col__address">Tannenfrost · E. Hallberger<br>Lindenauer Str. 14 · 74100 Wiesental<br><span class="col__web">www.tannenfrost.de</span></p>
  </div>
  <div class="col col--brand">
    <div class="brand__mark"></div>
    <div class="brand__name">TANNENFROST</div>
    <div class="brand__rule"></div>
    <div class="brand__tag">HONIG AUS DEUTSCHLAND</div>
    <div class="brand__variety">Blütenhonig</div>
    <div class="brand__note">Mit Linde &amp; Himbeere</div>
    <div class="brand__web">WWW.TANNENFROST.DE</div>
  </div>
  <div class="col col--facts">
    <div class="col__head">100% Honig aus Deutschland</div>
    <div class="facts__line" style="top:31px">Mehrwegglas</div>
    <div class="facts__line facts__weight" style="top:45px">400 g ℮</div>
    <div class="facts__line" style="top:67px">Trocken, dunkel und vor Wärme<br>geschützt lagern.</div>
    <div class="facts__line" style="top:94px">Mindestens haltbar bis / Los-Nr.:</div>
    <div class="facts__box"></div>
  </div>
</section>

<section class="label label--orange" style="top:551px">
  <div class="label__comb" role="img" aria-label="Dezentes Wabenmuster im Hintergrund"></div>
  <div class="col col--info">
    <div class="col__head">Bienenhonig aus der Region</div>
    <p class="col__text">Honig ist ein reines Naturprodukt ohne Zusätze. Diese Reinheit und Natürlichkeit sind in <b>Tannenfrost-Honig</b> vereint. Geniessen Sie goldene Momente mit ökologischem Natur-Honig aus eigener Ernte und regionalem Ursprung.</p>
    <div class="col__rule"></div>
    <p class="col__address">Tannenfrost · E. Hallberger<br>Lindenauer Str. 14 · 74100 Wiesental<br><span class="col__web">www.tannenfrost.de</span></p>
  </div>
  <div class="col col--brand">
    <div class="brand__mark"></div>
    <div class="brand__name">TANNENFROST</div>
    <div class="brand__rule"></div>
    <div class="brand__tag">HONIG AUS DEUTSCHLAND</div>
    <div class="brand__variety">Blütenhonig</div>
    <div class="brand__note">Cremig &amp; weich</div>
    <div class="brand__web">WWW.TANNENFROST.DE</div>
  </div>
  <div class="col col--facts">
    <div class="col__head">100% Honig aus Deutschland</div>
    <div class="facts__line" style="top:31px">Mehrwegglas</div>
    <div class="facts__line facts__weight" style="top:45px">400 g ℮</div>
    <div class="facts__line" style="top:67px">Trocken, dunkel und vor Wärme<br>geschützt lagern.</div>
    <div class="facts__line" style="top:94px">Mindestens haltbar bis / Los-Nr.:</div>
    <div class="facts__box"></div>
  </div>
</section>

<section class="label" style="top:739px">
  <div class="label__comb" role="img" aria-label="Dezentes Wabenmuster im Hintergrund"></div>
  <div class="col col--info">
    <div class="col__head">Bienenhonig aus der Region</div>
    <p class="col__text">Honig ist ein reines Naturprodukt ohne Zusätze. Diese Reinheit und Natürlichkeit sind in <b>Tannenfrost-Honig</b> vereint. Geniessen Sie goldene Momente mit ökologischem Natur-Honig aus eigener Ernte und regionalem Ursprung.</p>
    <div class="col__rule"></div>
    <p class="col__address">Tannenfrost · E. Hallberger<br>Lindenauer Str. 14 · 74100 Wiesental<br><span class="col__web">www.tannenfrost.de</span></p>
  </div>
  <div class="col col--brand">
    <div class="brand__mark"></div>
    <div class="brand__name">TANNENFROST</div>
    <div class="brand__rule"></div>
    <div class="brand__tag">HONIG AUS DEUTSCHLAND</div>
    <div class="brand__variety">Blütenhonig</div>
    <div class="brand__note">Mit Linde &amp; Himbeere</div>
    <div class="brand__web">WWW.TANNENFROST.DE</div>
  </div>
  <div class="col col--facts">
    <div class="col__head">100% Honig aus Deutschland</div>
    <div class="facts__line" style="top:31px">Mehrwegglas</div>
    <div class="facts__line facts__weight" style="top:45px">400 g ℮</div>
    <div class="facts__line" style="top:67px">Trocken, dunkel und vor Wärme<br>geschützt lagern.</div>
    <div class="facts__line" style="top:94px">Mindestens haltbar bis / Los-Nr.:</div>
    <div class="facts__box"></div>
  </div>
</section>

<section class="label label--green" style="top:928px">
  <div class="label__comb" role="img" aria-label="Dezentes Wabenmuster im Hintergrund"></div>
  <div class="col col--info">
    <div class="col__head">Bienenhonig aus der Region</div>
    <p class="col__text">Honig ist ein reines Naturprodukt ohne Zusätze. Diese Reinheit und Natürlichkeit sind in <b>Tannenfrost-Honig</b> vereint. Geniessen Sie goldene Momente mit ökologischem Natur-Honig aus eigener Ernte und regionalem Ursprung.</p>
    <div class="col__rule"></div>
    <p class="col__address">Tannenfrost · E. Hallberger<br>Lindenauer Str. 14 · 74100 Wiesental<br><span class="col__web">www.tannenfrost.de</span></p>
  </div>
  <div class="col col--brand">
    <div class="brand__mark"></div>
    <div class="brand__name">TANNENFROST</div>
    <div class="brand__rule"></div>
    <div class="brand__tag">HONIG AUS DEUTSCHLAND</div>
    <div class="brand__variety">Waldhonig</div>
    <div class="brand__note">Kräftig &amp; herzhaft</div>
    <div class="brand__web">WWW.TANNENFROST.DE</div>
  </div>
  <div class="col col--facts">
    <div class="col__head">100% Honig aus Deutschland</div>
    <div class="facts__line" style="top:31px">Mehrwegglas</div>
    <div class="facts__line facts__weight" style="top:45px">400 g ℮</div>
    <div class="facts__line" style="top:67px">Trocken, dunkel und vor Wärme<br>geschützt lagern.</div>
    <div class="facts__line" style="top:94px">Mindestens haltbar bis / Los-Nr.:</div>
    <div class="facts__box"></div>
  </div>
</section>

<div class="footer">ETIKETTEN „TANNENFROST“ ABMESSUNG 180 X 44 MM · WWW.TANNENFROST.DE</div>

</body>
</html>
```